I would like a site similar to this: http://www.givewheelsforheroes.example

old site: http://www.autosforpatriots.example

Create a professional website; a car donation site seeking leads to return calls.

Please see http://www.givewheelsforheroes.example for the concept I am after.

The webpage should have a professional feel. The pages to include are 'Home', 'About us' and 'Get Started'

Industry/Entity Type

It Professional

Coding

Coded - Design and coding required

Number of Pages Required

1 page

```html
<!DOCTYPE html>
<html lang="en">
<head>
<meta charset="utf-8">
<title>Autos For Patriots – Donate Your Car</title>
<link href="https://fonts.googleapis.com/css2?family=Montserrat:wght@600;700;800&family=Open+Sans:wght@400;600;700&display=swap" rel="stylesheet">
<style>
:root{
  --navy:#1a3a8e;
  --navy-dark:#12265f;
  --red:#a5150f;
  --red-dark:#8d120c;
  --gold:#c8a45c;
  --ink:#2b2b2b;
  --muted:#555;
  --line:#d4d4d4;
  --frame:#e9e9e9;
  --white:#fff;
}
*{box-sizing:border-box;margin:0;padding:0}
html,body{width:1200px;height:2643px;overflow:hidden}
body{background:var(--frame);font-family:"Open Sans",Arial,sans-serif;color:var(--ink);position:relative}
.abs{position:absolute}
.page{position:absolute;left:14px;top:14px;width:1172px;height:2615px;background:var(--white);overflow:hidden}
/* header */
.header{left:0;top:0;width:1172px;height:153px;background:linear-gradient(100deg,#13286a 0%,#2a4a9a 35%,#7a2a30 70%,#3a2a50 100%)}
.logo{left:44px;top:52px;display:flex;align-items:center;gap:12px}
.logo-mark{width:34px;height:34px;background:var(--red);border-radius:4px}
.logo-name{font-family:Montserrat,Arial,sans-serif;font-weight:800;font-size:30px;color:var(--white);letter-spacing:.5px}
.nav{left:0;top:153px;width:1172px;height:44px;background:var(--navy)}
.nav a{position:absolute;top:12px;font-family:Montserrat,Arial,sans-serif;font-weight:700;font-size:14px;color:var(--white);text-decoration:none}
/* hero */
.hero{left:0;top:197px;width:775px;height:388px;background:linear-gradient(180deg,#b9cfe0 0%,#dfe6ea 55%,#a9a49a 100%)}
/* donate panel */
.panel{left:774px;top:0;width:352px;height:585px;background:var(--red)}
.call{left:22px;top:36px;display:flex;gap:14px;align-items:center}
.call-icon{width:64px;height:64px;border:3px solid var(--white);border-radius:50%;display:flex;align-items:center;justify-content:center}
.call-text{font-family:Montserrat,Arial,sans-serif;color:var(--white);line-height:1.1}
.call-text .t1{font-size:17px;font-weight:700}
.call-text .t2{font-size:29px;font-weight:800}
.call-text .t3{font-size:11px;font-weight:600}
.car-dot{left:158px;top:138px;width:36px;height:30px;background:var(--red);border-radius:50% 50% 0 0;display:flex;justify-content:center;padding-top:6px}
.tab{left:-13px;top:153px;width:378px;height:44px;background:var(--white);font-family:Montserrat,Arial,sans-serif;font-weight:700;font-size:18px;color:var(--red);text-align:center;line-height:44px}
.panel-title{left:0;top:222px;width:352px;text-align:center;font-family:Montserrat,Arial,sans-serif;font-weight:700;font-size:15px;color:var(--white)}
.field{position:absolute;height:29px;background:var(--white);border-radius:3px;font-size:12px;font-weight:600;color:#333;padding:6px 6px;display:flex;justify-content:space-between}
.field.half{width:153px}
.field.full{width:315px;left:19px}
.field .caret{width:0;height:0;border-left:5px solid transparent;border-right:5px solid transparent;border-top:6px solid #555;margin-top:5px}
.btn{left:21px;top:518px;width:151px;height:40px;background:var(--navy-dark);border-radius:3px;color:var(--white);font-family:Montserrat,Arial,sans-serif;font-weight:700;font-size:14px;text-align:center;line-height:40px}
/* banner */
.banner{left:0;top:585px;width:1172px;height:211px;background:linear-gradient(180deg,#f2f2f2,#cfd0d2)}
.ribbon{left:0;top:0;width:515px;height:211px}
.ribbon-text{left:58px;top:30px;font-family:Montserrat,Arial,sans-serif;color:var(--white);font-weight:700}
.ribbon-text .r1{font-size:27px}
.ribbon-text .r2{font-size:52px;font-weight:800;color:var(--gold);line-height:1.05}
.ribbon-text .r3{font-size:27px}
.feature{position:absolute;top:52px;width:140px;text-align:center}
.feature p{margin-top:12px;font-family:Montserrat,Arial,sans-serif;font-weight:700;font-size:12px;line-height:1.3;color:var(--red);white-space:nowrap}
/* sections */
.section-title{position:absolute;left:0;width:1172px;text-align:center;font-family:Montserrat,Arial,sans-serif;font-weight:800;font-size:27px;color:var(--navy)}
.section-title span{color:var(--red)}
.section-title::before,.section-title::after{content:"";display:inline-block;width:100px;height:1px;background:var(--line);vertical-align:middle;margin:0 26px}
.step{position:absolute;top:920px;width:350px;display:flex;gap:16px}
.step h3{font-family:Montserrat,Arial,sans-serif;font-weight:700;font-size:15px;color:var(--navy);line-height:1.3;margin-bottom:12px}
.step p{font-size:13px;font-weight:600;line-height:1.45;color:#333}
.why{left:0;top:1131px;width:1172px;height:405px;background:linear-gradient(180deg,#e6e6e8 0%,#f4efe6 55%,#ddd9d2 100%)}
.why-list{left:148px;top:140px;list-style:none}
.why-list li{display:flex;align-items:center;gap:12px;height:32px;font-size:13.5px;color:#333}
.why-list b{font-weight:700}
.bullet{width:20px;height:20px;border-radius:50%;background:var(--red);display:flex;align-items:center;justify-content:center;flex:none}
.faq-photo{left:79px;top:1665px;width:506px;height:414px;background:linear-gradient(160deg,#b8423f 0%,#e8e4e2 35%,#2a3f7a 60%,#8b7a5e 100%)}
.faq{left:619px;top:1665px;width:474px}
.faq-item{border:1px solid var(--line);border-radius:9px;margin-bottom:8px;padding:9px 14px;box-shadow:0 1px 2px rgba(0,0,0,.08)}
.faq-q{display:flex;justify-content:space-between;align-items:center;gap:10px;font-family:Montserrat,Arial,sans-serif;font-weight:700;font-size:13.5px;color:#333}
.faq-q svg{flex:none}
.faq-a{font-size:13px;line-height:1.45;color:#555;margin-top:6px}
/* footer */
.footer{left:0;top:2180px;width:1172px;height:396px;background:linear-gradient(160deg,#1d3f9a 0%,#173482 50%,#2b4ea6 100%)}
.footer-tab{left:320px;top:2136px;width:532px;height:70px;background:#1d3f9a;border-radius:46px 46px 0 0}
.footer-logo{left:0;top:2152px;width:1172px;display:flex;justify-content:center;align-items:center;gap:12px}
.fcol{position:absolute;top:2298px;color:var(--white)}
.fcol h4{font-family:Montserrat,Arial,sans-serif;font-weight:700;font-size:13px;padding-bottom:10px;border-bottom:1px solid rgba(255,255,255,.35);margin-bottom:12px}
.fcol p{font-size:11.5px;font-weight:600;line-height:1.4}
.fcol a{display:block;color:var(--white);text-decoration:none;font-family:Montserrat,Arial,sans-serif;font-size:12px;font-weight:600;line-height:1.4}
.badge{display:block;background:rgba(255,255,255,.9);border-radius:4px;margin-bottom:12px}
.fcall{left:761px;top:2301px;width:342px;height:143px;border:2px solid var(--white);border-radius:10px;display:flex;align-items:center;justify-content:center;gap:14px}
.copyright{left:0;top:2576px;width:1172px;height:39px;background:var(--white);text-align:center;line-height:39px;font-family:Montserrat,Arial,sans-serif;font-weight:700;font-size:10.5px;color:#333}
</style>
</head>
<body>
<div class="page">
  <header class="header abs">
    <div class="logo abs"><span class="logo-mark"></span><span class="logo-name">AUTOS FOR PATRIOTS</span></div>
  </header>
  <nav class="nav abs">
    <a href="#how" style="left:175px">HOW TO DONATE</a>
    <a href="#why" style="left:356px">WHY DONATE</a>
    <a href="#faq" style="left:511px">FAQ</a>
    <a href="#about" style="left:596px">ABOUT</a>
  </nav>
  <div class="hero abs" role="img" aria-label="Soldier embracing a child holding a small flag, with a pickup truck and a red classic car in front of a city skyline"></div>

  <aside class="panel abs">
    <div class="call abs">
      <div class="call-icon"><svg width="32" height="32" viewBox="0 0 24 24"><path fill="#fff" d="M6.6 10.8c1.4 2.8 3.8 5.1 6.6 6.6l2.2-2.2c.3-.3.7-.4 1-.2 1.1.4 2.3.6 3.6.6.6 0 1 .4 1 1V20c0 .6-.4 1-1 1C10.6 21 3 13.4 3 4c0-.6.4-1 1-1h3.5c.6 0 1 .4 1 1 0 1.3.2 2.5.6 3.6.1.3 0 .7-.2 1z"/></svg></div>
      <div class="call-text"><div class="t1">CALL TODAY TO DONATE</div><div class="t2">1-800-555-0142</div><div class="t3">Live Operators Available - 7 Days A Week</div></div>
    </div>
    <div class="car-dot abs"><svg width="20" height="14" viewBox="0 0 20 14"><path fill="#fff" d="M3 6l2-5h10l2 5h1v6h-3v2h-2v-2H7v2H5v-2H2V6zm3-1h8l-1-3H7z"/></svg></div>
    <div class="tab abs">DONATE YOUR CAR ONLINE</div>
    <div class="panel-title abs">Full Tax Deduction - Running or Not</div>
    <div class="field half" style="left:19px;top:254px">First Name</div>
    <div class="field half" style="left:181px;top:254px">Last Name</div>
    <div class="field half" style="left:19px;top:291px">Daytime Phone</div>
    <div class="field half" style="left:181px;top:291px">Email</div>
    <div class="field full" style="top:328px">Pickup Address</div>
    <div class="field full" style="top:365px">Pickup City</div>
    <div class="field half" style="left:19px;top:402px">Pickup State<span class="caret"></span></div>
    <div class="field half" style="left:181px;top:402px">Zip Code</div>
    <div class="field half" style="left:19px;top:439px">Choose Year<span class="caret"></span></div>
    <div class="field half" style="left:181px;top:439px">Choose Make<span class="caret"></span></div>
    <div class="field full" style="top:476px">Vehicle Model</div>
    <div class="btn abs">DONATE NOW</div>
  </aside>

  <section class="banner abs">
    <svg class="ribbon abs" viewBox="0 0 515 211"><defs><linearGradient id="rib" x1="0" x2="1" y1="0" y2="1"><stop offset="0" stop-color="#2b4fa8"/><stop offset="1" stop-color="#14286b"/></linearGradient></defs><path d="M0 0H420L515 211H0Z" fill="url(#rib)"/><path d="M455 180L515 211H470Z" fill="#0c1a4a"/></svg>
    <div class="ribbon-text abs"><div class="r1">DONATE YOUR CAR TO</div><div class="r2">VETERANS</div><div class="r3">MAKE A DIFFERENCE</div></div>
    <div class="feature" style="left:497px"><svg width="60" height="60" viewBox="0 0 60 60"><circle cx="30" cy="30" r="25" fill="none" stroke="#1a3a8e" stroke-width="4"/><path d="M18 30l9 9 18-20" fill="none" stroke="#1a3a8e" stroke-width="5"/></svg><p>You have<br>no costs</p></div>
    <div class="feature" style="left:626px"><svg width="60" height="60" viewBox="0 0 60 60"><path d="M6 40V28l8-10h10v22z" fill="#1a3a8e"/><path d="M24 40l26-18v18z" fill="#1a3a8e"/><circle cx="16" cy="44" r="6" fill="#a5150f"/><circle cx="44" cy="44" r="6" fill="#a5150f"/><path d="M24 10l14 12" stroke="#1a3a8e" stroke-width="3"/></svg><p>Free towing,<br>running or not</p></div>
    <div class="feature" style="left:755px"><svg width="60" height="60" viewBox="0 0 60 60"><rect x="14" y="6" width="32" height="48" rx="2" fill="none" stroke="#1a3a8e" stroke-width="3"/><text x="30" y="32" text-anchor="middle" font-family="Montserrat,sans-serif" font-weight="700" font-size="16" fill="#1a3a8e">$</text><path d="M20 40h20M20 46h20" stroke="#1a3a8e" stroke-width="2"/></svg><p>We issue you an<br>IRS tax receipt</p></div>
    <div class="feature" style="left:883px"><svg width="60" height="60" viewBox="0 0 60 60"><rect x="22" y="6" width="30" height="44" rx="2" fill="none" stroke="#1a3a8e" stroke-width="3"/><circle cx="22" cy="30" r="10" fill="#fff" stroke="#1a3a8e" stroke-width="3"/><path d="M15 37L6 48" stroke="#1a3a8e" stroke-width="5"/><path d="M30 14h16M36 22h10" stroke="#1a3a8e" stroke-width="2"/></svg><p>We take care of<br>all paperwork.</p></div>
    <div class="feature" style="left:1012px"><svg width="60" height="60" viewBox="0 0 60 60"><rect x="14" y="10" width="32" height="44" rx="2" fill="none" stroke="#1a3a8e" stroke-width="3"/><rect x="23" y="5" width="14" height="9" rx="2" fill="#1a3a8e"/><path d="M20 24h20M20 32h20M20 40h14" stroke="#1a3a8e" stroke-width="2"/></svg><p>We take care of<br>DMV &amp; Smog issues</p></div>
  </section>

  <h2 id="how" class="section-title" style="top:852px">HOW TO <span>DONATE</span></h2>
  <div class="step" style="left:60px"><svg width="90" height="90" viewBox="0 0 90 90" style="flex:none"><rect x="28" y="4" width="40" height="10" fill="#a5150f"/><rect x="28" y="22" width="40" height="10" fill="#a5150f"/><rect x="28" y="40" width="40" height="10" fill="#a5150f"/><path d="M6 72l16-22 4 14 14 2z" fill="#a5150f"/></svg><div><h3>CALL US AT 1-800-555-0142 OR<br>FILL OUT THE ONLINE FORM</h3><p>Donating your vehicle is easy and<br>donation is accepted nationwide.</p></div></div>
  <div class="step" style="left:435px"><svg width="90" height="90" viewBox="0 0 90 90" style="flex:none"><path d="M4 58V36l10-14h18v36z" fill="#a5150f"/><path d="M32 58l40-26v26z" fill="#a5150f"/><path d="M50 8l20 18" stroke="#a5150f" stroke-width="5"/><circle cx="18" cy="62" r="8" fill="#fff" stroke="#a5150f" stroke-width="4"/><circle cx="60" cy="62" r="8" fill="#fff" stroke="#a5150f" stroke-width="4"/></svg><div><h3>WE TOW THE VEHICLE</h3><p>Any vehicles is accepted and we will<br>arrange to pick up your vehicle when<br>it is most convenient for you.</p></div></div>
  <div class="step" style="left:828px"><svg width="90" height="90" viewBox="0 0 90 90" style="flex:none"><rect x="18" y="6" width="36" height="60" fill="none" stroke="#a5150f" stroke-width="3"/><rect x="10" y="14" width="36" height="60" fill="#fff" stroke="#a5150f" stroke-width="3"/><text x="28" y="44" text-anchor="middle" font-family="Montserrat,sans-serif" font-weight="800" font-size="20" fill="#a5150f">$</text><path d="M16 54h24M16 62h24" stroke="#a5150f" stroke-width="2"/></svg><div><h3>TAX WRITE-OFF</h3><p>Once the vehicle donation is<br>complete, you will receive your<br>tax deductable vehicle donation<br>receipt.</p></div></div>

  <section id="why" class="why abs" role="img" aria-label="Soldiers silhouetted against a sunlit sky raising a large flag">
    <h2 class="section-title" style="top:53px">WHY DONATE <span>YOUR CAR TO US</span></h2>
    <ul class="why-list abs">
      <li><span class="bullet"><svg width="10" height="10" viewBox="0 0 10 10"><path d="M2 5h6M5 2l3 3-3 3" stroke="#fff" stroke-width="2" fill="none"/></svg></span><span><b>Top Rated &amp; IRS 501(c)3 Approved :</b> Free 24/7 Pickup with No DMV Hassles.</span></li>
      <li><span class="bullet"><svg width="10" height="10" viewBox="0 0 10 10"><path d="M2 5h6M5 2l3 3-3 3" stroke="#fff" stroke-width="2" fill="none"/></svg></span><span><b>Free Local Towing :</b> We will pick up your car donation, running or not, when it's most convenient, at home or work.</span></li>
      <li><span class="bullet"><svg width="10" height="10" viewBox="0 0 10 10"><path d="M2 5h6M5 2l3 3-3 3" stroke="#fff" stroke-width="2" fill="none"/></svg></span><span><b>All Cars Accepted :</b> We take your car regardless of its condition or registration status.</span></li>
      <li><span class="bullet"><svg width="10" height="10" viewBox="0 0 10 10"><path d="M2 5h6M5 2l3 3-3 3" stroke="#fff" stroke-width="2" fill="none"/></svg></span><span><b>Income Tax Deduction :</b> We issue you an IRS tax receipt &amp; offer the largest resale network to get you the highest tax write-off possible.</span></li>
      <li><span class="bullet"><svg width="10" height="10" viewBox="0 0 10 10"><path d="M2 5h6M5 2l3 3-3 3" stroke="#fff" stroke-width="2" fill="none"/></svg></span><span><b>No Paperwork Hassles :</b> We take any car and handle everything: DMV, Smog and IRS paperwork.</span></li>
      <li><span class="bullet"><svg width="10" height="10" viewBox="0 0 10 10"><path d="M2 5h6M5 2l3 3-3 3" stroke="#fff" stroke-width="2" fill="none"/></svg></span><span><b>Car donations help fund programs :</b> And benefit National Heroes Support Fund. An IRS 501(c)3 nonprofit organization.</span></li>
      <li><span class="bullet"><svg width="10" height="10" viewBox="0 0 10 10"><path d="M2 5h6M5 2l3 3-3 3" stroke="#fff" stroke-width="2" fill="none"/></svg></span><span><b>Schedule a Free Pickup :</b> Complete the form and a representative will call you to arrange a convenient time to pickup your car.</span></li>
    </ul>
  </section>

  <h2 id="faq" class="section-title" style="top:1588px">FREQUENTLY ASKED <span>QUESTIONS</span></h2>
  <div class="faq-photo abs" role="img" aria-label="Marching soldiers' boots beneath a waving striped flag"></div>
  <div class="faq abs">
    <div class="faq-item"><div class="faq-q">What types of vehicles can be donated?<svg width="12" height="8" viewBox="0 0 12 8"><path d="M1 1l5 5 5-5" stroke="#333" stroke-width="2" fill="none"/></svg></div></div>
    <div class="faq-item"><div class="faq-q">What paperwork do I need to donate my vehicle?<svg width="12" height="8" viewBox="0 0 12 8"><path d="M1 7l5-5 5 5" stroke="#333" stroke-width="2" fill="none"/></svg></div><p class="faq-a">All you need is a title, free of all liens. We will request some general information from you at the time of donation such as, the year, make, and model of the car, as well as its general mechanical condition. We accept all vehicles, running or non-running.</p></div>
    <div class="faq-item"><div class="faq-q">Is my donated vehicle tax -deductible?<svg width="12" height="8" viewBox="0 0 12 8"><path d="M1 1l5 5 5-5" stroke="#333" stroke-width="2" fill="none"/></svg></div></div>
    <div class="faq-item"><div class="faq-q">What if the vehicle is not registered in my name?<svg width="12" height="8" viewBox="0 0 12 8"><path d="M1 1l5 5 5-5" stroke="#333" stroke-width="2" fill="none"/></svg></div></div>
    <div class="faq-item"><div class="faq-q">How much will I receive as a tax deduction for my vehicle?<svg width="12" height="8" viewBox="0 0 12 8"><path d="M1 1l5 5 5-5" stroke="#333" stroke-width="2" fill="none"/></svg></div></div>
    <div class="faq-item"><div class="faq-q">When will I receive my tax receipt?<svg width="12" height="8" viewBox="0 0 12 8"><path d="M1 1l5 5 5-5" stroke="#333" stroke-width="2" fill="none"/></svg></div></div>
    <div class="faq-item"><div class="faq-q">How do I schedule a pick up?<svg width="12" height="8" viewBox="0 0 12 8"><path d="M1 1l5 5 5-5" stroke="#333" stroke-width="2" fill="none"/></svg></div></div>
  </div>

  <div class="footer-tab abs"></div>
  <footer class="footer abs"></footer>
  <div class="footer-logo abs"><span class="logo-mark"></span><span class="logo-name">AUTOS FOR PATRIOTS</span></div>
  <div id="about" class="fcol" style="left:71px;width:245px"><h4>ABOUT AUTOS FOR PATRIOTS</h4><p>Lorem ipsum dolor sit amet, consectetuer adipiscing elit, sed diam nonummy nibheu euismod tincidunt ut laoreet dolore magna aliquam erat volutpat. Ut wisi enim ad mini veniam, quis nostrud exerci tation ullamcor per suscipit lobortis nisl ut aliquip ex ea co modo consequat.</p></div>
  <div class="fcol" style="left:372px;width:125px"><h4>NAVIGATION</h4><a href="#how">HOW TO DONATE</a><a href="#why">WHY DONATE</a><a href="#faq">FAQ</a><a href="#about">ABOUT</a></div>
  <div class="fcol" style="left:543px;width:160px"><h4>SAFE &amp; SECURE</h4><span class="badge" style="width:155px;height:48px"></span><span class="badge" style="width:120px;height:40px"></span><span class="badge" style="width:48px;height:48px;border-radius:50%"></span></div>
  <div class="fcall abs">
    <div class="call-icon"><svg width="32" height="32" viewBox="0 0 24 24"><path fill="#fff" d="M6.6 10.8c1.4 2.8 3.8 5.1 6.6 6.6l2.2-2.2c.3-.3.7-.4 1-.2 1.1.4 2.3.6 3.6.6.6 0 1 .4 1 1V20c0 .6-.4 1-1 1C10.6 21 3 13.4 3 4c0-.6.4-1 1-1h3.5c.6 0 1 .4 1 1 0 1.3.2 2.5.6 3.6.1.3 0 .7-.2 1z"/></svg></div>
    <div class="call-text"><div class="t1">CALL TODAY TO DONATE</div><div class="t2">1-800-555-0142</div><div class="t3">Live Operators Available - 7 Days A Week</div></div>
  </div>
  <div class="copyright abs">COPYRIGHT © 2016 AUTOS FOR PATRIOTS. PRIVACY POLICY I TERMS &amp; CONDITIONS. ALL RIGHTS RESERVED.</div>
</div>
</body>
</html>
```